New Menu for Elegant Cafe Pastry Shop

We need to choose a design and layout for our new menu. We would like to also condense our current menu to 4-6 pages.
We will be changing prices and items on the menu, so it needs to be editable. Adobe formats are preferred. The size of the pages needs to be letter size. We will be printing it in house
Please take inspiration from the photos of our shop and food and also our Picmosaic page.
Attached are our current menu our logo and the logo info

https://www.picmosaic.com/marbrecoquette/?hl=en
https://maps.wayfindr.app/Qk3Lm9Xp2Tb7VwR4a

Industry/Entity Type

Food Cafe Bakery pastry

Other font styles liked:
• please look at attached files

Colors

Designer to choose colors to be used in the design.

Requirements
Nice to have
• Use of Arches like on our shop wallpaper or oblong eclair shapes, Art Deco elements

```html
<!DOCTYPE html>
<html lang="en">
<head>
<meta charset="utf-8">
<title>Marbre Coquette — Seasonal Menu</title>
<link rel="stylesheet" href="https://fonts.googleapis.com/css2?family=Jost:wght@200;300;400;500&display=swap">
<style>
  :root {
    --teal: #45c3cd;
    --teal-light: #a0f5fb;
    --paper: #ffffff;
    --ink: #111111;
    --ink-soft: #555555;
    --plum: #3a1f2e;
  }
  * { margin: 0; padding: 0; box-sizing: border-box; }
  html, body { width: 927px; height: 1200px; overflow: hidden; background: var(--teal); }
  body { font-family: "Jost", sans-serif; color: var(--ink); }

  .menu-page { position: relative; width: 927px; height: 1200px; background: var(--teal); }
  .frame-inner { position: absolute; left: 22px; top: 22px; right: 22px; bottom: 22px; background: var(--teal-light); }
  .sheet { position: absolute; left: 33px; top: 33px; right: 33px; bottom: 33px; background: var(--paper); }

  .rules { position: absolute; left: 0; top: 0; width: 927px; height: 1200px; pointer-events: none; }
  .rules line { stroke: var(--teal); stroke-width: 0.8; }

  .abs { position: absolute; white-space: nowrap; }

  .brand { left: 0; width: 927px; top: 188px; display: flex; justify-content: center; align-items: center; gap: 12px; }
  .brand-dot { width: 22px; height: 22px; border-radius: 50%; background: var(--teal); }
  .brand-name { font-size: 32px; font-weight: 400; letter-spacing: 2px; color: var(--plum); text-transform: uppercase; }

  .page-title { left: 0; width: 927px; top: 322px; text-align: center; font-size: 92px; font-weight: 200; letter-spacing: 15px; padding-left: 15px; line-height: 1; }
  .page-note { left: 0; width: 927px; top: 415px; text-align: center; font-size: 12px; font-weight: 300; }

  .item-name { font-size: 15px; font-weight: 500; letter-spacing: 0.4px; line-height: 1; text-transform: uppercase; display: flex; align-items: center; gap: 4px; }
  .item-desc { font-size: 12px; font-weight: 300; color: var(--ink-soft); line-height: 14.5px; }
  .price { font-size: 15.5px; font-weight: 300; line-height: 1; }
  .price.right { text-align: right; }

  .tag { display: inline-flex; align-items: center; justify-content: center; width: 19px; height: 19px; border: 1px solid var(--teal); border-radius: 50%; font-size: 8px; font-weight: 400; color: var(--teal); letter-spacing: 0; }

  .section-title { font-size: 38px; font-weight: 200; line-height: 1; letter-spacing: 0.5px; }
  .section-note { font-size: 12px; font-weight: 300; }
  .pill { background: var(--teal); color: #fff; border-radius: 8px; font-size: 11px; font-weight: 300; padding: 0 4px; line-height: 13px; }

  .drink-name { font-size: 15px; font-weight: 500; letter-spacing: 0.4px; text-transform: uppercase; line-height: 1; }

  .legend-item { width: 130px; text-align: center; display: flex; flex-direction: column; align-items: center; gap: 3px; top: 1126px; }
  .legend-item .tag { width: 19px; height: 19px; }
  .legend-label { font-size: 9px; font-weight: 400; letter-spacing: 0.2px; }
</style>
</head>
<body>
<main class="menu-page">
  <div class="frame-inner"></div>
  <div class="sheet"></div>

  <svg class="rules" viewBox="0 0 927 1200" aria-hidden="true">
    <line x1="72" y1="489" x2="854" y2="489"/>
    <line x1="72" y1="600" x2="854" y2="600"/>
    <!-- travel cakes -->
    <line x1="74" y1="676" x2="98" y2="676"/>
    <line x1="98" y1="672" x2="122" y2="672"/><line x1="98" y1="676" x2="122" y2="676"/><line x1="98" y1="680" x2="122" y2="680"/>
    <line x1="376" y1="672" x2="400" y2="672"/><line x1="376" y1="676" x2="400" y2="676"/><line x1="376" y1="680" x2="400" y2="680"/>
    <line x1="400" y1="676" x2="423" y2="676"/>
    <!-- baba au rhum -->
    <line x1="503" y1="676" x2="525" y2="676"/>
    <line x1="525" y1="672" x2="547" y2="672"/><line x1="525" y1="676" x2="547" y2="676"/><line x1="525" y1="680" x2="547" y2="680"/>
    <line x1="811" y1="672" x2="833" y2="672"/><line x1="811" y1="676" x2="833" y2="676"/><line x1="811" y1="680" x2="833" y2="680"/>
    <line x1="833" y1="676" x2="855" y2="676"/>
    <!-- mocktails -->
    <line x1="75" y1="946" x2="219" y2="946"/>
    <line x1="219" y1="941" x2="362" y2="941"/><line x1="219" y1="946" x2="362" y2="946"/><line x1="219" y1="951" x2="362" y2="951"/>
    <line x1="563" y1="941" x2="709" y2="941"/><line x1="563" y1="946" x2="709" y2="946"/><line x1="563" y1="951" x2="709" y2="951"/>
    <line x1="709" y1="946" x2="855" y2="946"/>
    <!-- legend dividers -->
    <line x1="277" y1="1123" x2="277" y2="1159"/>
    <line x1="422" y1="1123" x2="422" y2="1159"/>
    <line x1="555" y1="1123" x2="555" y2="1159"/>
    <line x1="683" y1="1123" x2="683" y2="1159"/>
  </svg>

  <header>
    <div class="abs brand"><span class="brand-dot"></span><span class="brand-name">Marbre Coquette</span></div>
    <h1 class="abs page-title">SEASONAL</h1>
    <p class="abs page-note">(Upon availability)</p>
  </header>

  <section class="seasonal">
    <div class="abs item-name" style="left:105px; top:520px;">Pistachio Raspberry Opera <span class="tag">CN</span></div>
    <p class="abs item-desc" style="left:105px; top:540px;">Pistachio joconde cake layered with pistachio<br>buttercream, chocolate ganache and raspberry gelée.</p>
    <div class="abs price" style="left:446px; top:521px;">$ 8.80</div>
    <div class="abs item-name" style="left:614px; top:523px;">Lorraine</div>
    <div class="abs price" style="left:782px; top:521px;">$6.99</div>
  </section>

  <section class="travel-cakes">
    <h2 class="abs section-title" style="left:122px; top:657px;">TRAVEL CAKES</h2>
    <span class="abs pill" style="left:227px; top:694px;">Vegan</span>
    <div class="abs item-name" style="left:72px; top:736px;">Banana Pecan <span class="tag">CN</span></div>
    <div class="abs price right" style="left:344px; width:80px; top:738px;">$6.00</div>
    <div class="abs item-name" style="left:72px; top:775px;">Banana Walnut <span class="tag">CN</span></div>
    <div class="abs price right" style="left:344px; width:80px; top:777px;">$6.00</div>
    <div class="abs item-name" style="left:72px; top:815px;">Banana Chocolate Chips</div>
    <div class="abs price right" style="left:344px; width:80px; top:815px;">$6.00</div>
    <div class="abs item-name" style="left:72px; top:854px;">Blueberry</div>
    <div class="abs price right" style="left:344px; width:80px; top:854px;">$6.00</div>
  </section>

  <section class="baba-au-rhum">
    <h2 class="abs section-title" style="left:548px; top:657px;">BABA AU RHUM</h2>
    <p class="abs section-note" style="left:548px; width:262px; text-align:center; top:693px;">(Contain Alcohol)</p>
    <div class="abs item-name" style="left:503px; top:739px;">Chocolate / Noisella</div>
    <div class="abs price right" style="left:775px; width:80px; top:738px;">$7.80</div>
    <div class="abs item-name" style="left:503px; top:778px;">Vanilla/Orange/Pineapple</div>
    <div class="abs price right" style="left:775px; width:80px; top:777px;">$7.80</div>
  </section>

  <section class="mocktails">
    <h2 class="abs section-title" style="left:363px; top:928px;">MOCKTAILS</h2>
    <div class="abs drink-name" style="left:74px; top:988px;">Pina Colada</div>
    <p class="abs item-desc" style="left:74px; top:1006px;">A tropical classic mocktail<br>of pineapple and coconut</p>
    <div class="abs price" style="left:73px; top:1059px;">$ 6.30</div>
    <div class="abs drink-name" style="left:379px; top:988px;">Mango Lychee</div>
    <p class="abs item-desc" style="left:379px; top:1006px;">Refreshing mix of lychee<br>and mango</p>
    <div class="abs price" style="left:379px; top:1059px;">$ 6.50</div>
    <div class="abs drink-name" style="left:665px; top:988px;">Scarlet Fizz</div>
    <p class="abs item-desc" style="left:665px; top:1006px;">Ginger ale and grenadine mocktail<br>garnished with maraschino cherry</p>
    <div class="abs price" style="left:665px; top:1059px;">$ 6.30</div>
  </section>

  <footer class="legend">
    <div class="abs legend-item" style="left:153px;"><span class="tag">CN</span><span class="legend-label">CONTAINS NUTS</span></div>
    <div class="abs legend-item" style="left:287px;"><span class="tag">CA</span><span class="legend-label">CONTAINS ALMONDS</span></div>
    <div class="abs legend-item" style="left:421px;"><span class="tag">CW</span><span class="legend-label">CONTAINS WALNUTS</span></div>
    <div class="abs legend-item" style="left:555px;"><span class="tag">GF</span><span class="legend-label">GLUTEN FREE</span></div>
    <div class="abs legend-item" style="left:666px;"><span class="tag">V</span><span class="legend-label">VEGAN</span></div>
  </footer>
</main>
</body>
</html>
```